Plumbing Business Card Design

our business is a plumbing business.
we would like to see designs with our LOGO featured and then either purple or black writing with a white back ground
or black back ground with white or purple writing or even a purple card!
one option we would love to see is if you could get the KTW letters away from the white background ( it is currently in a white box as a jpeg )it is currently on and overlay it onto black.
FRONT
KTW image to be displayed on the front, please use the attached picture. ( you can remove the email address and mobile number from the botttom and re write it in different font or in a different place on the front.
Directly under the large KTW we would like the words Copper Linton Plumbing.
could be spread out like this C O P P E R L I N T O N
P L U M B I N G
We really are open to suggestions though!
Also on the front of the card we could like our little catch phrase somewhere Borra's Trusted Plumber

we dont want in plumbing pictures or photos but we are open to swirl across the card or water movement or droplets.

BACK
These services need to be dot pointed or listed on the back
Hot & Cold Water Services
Gas Fitting
Bathroom & Kitchen Renovations
Metal Roofing & Guttering
New Homes & Extensions
Hot Water Service Changeovers
Drainage & Stormwater Works
All General Plumbing & Maitenance

in smaller writing or down the bottom of the card on the back please display write this Lic. No 492318

Contact Information for Business Card

Reid Linton
Mobile: 0427 316 902
email: copperlintonplumbing@mailvane.example
FInd Us on Facebook Copper Linton Plumbing ( with the f symbol ) either on the front or the back

```html
<!DOCTYPE html>
<html lang="en">
<head>
<meta charset="utf-8">
<title>Copper Linton Plumbing – Business Card</title>
<link rel="stylesheet" href="https://fonts.googleapis.com/css2?family=Open+Sans:wght@400;600;700&display=swap">
<style>
  :root {
    --page: #9b9b9b;
    --card: #ebebee;
    --blue: #1670e0;
    --purple: #6a12e0;
    --white: #ffffff;
    --ink: #474747;
  }
  * { box-sizing: border-box; margin: 0; padding: 0; }
  html, body { width: 1105px; height: 1200px; overflow: hidden; }
  body {
    background: var(--page);
    font-family: "Open Sans", Arial, sans-serif;
    position: relative;
  }
  .card {
    position: absolute;
    left: 180px;
    width: 746px;
    height: 426px;
    background: var(--card);
    overflow: hidden;
  }
  .card--front { top: 120px; }
  .card--back { top: 636px; }

  .wave { position: absolute; inset: 0; width: 100%; height: 100%; }

  .brand {
    position: absolute;
    left: 83px;
    top: 78px;
    width: 254px;
    text-align: center;
  }
  .brand__mark {
    font-weight: 700;
    font-size: 96px;
    line-height: 1;
    letter-spacing: 10px;
    color: var(--blue);
  }
  .brand__name {
    margin-top: 10px;
    font-weight: 700;
    font-size: 13px;
    letter-spacing: 2.6px;
    color: var(--blue);
    white-space: nowrap;
  }

  .contact {
    position: absolute;
    right: 46px;
    top: 254px;
    color: var(--white);
    text-align: right;
  }
  .contact__name {
    font-weight: 600;
    font-size: 24px;
    margin-right: 32px;
    margin-bottom: 8px;
  }
  .contact__line {
    display: flex;
    justify-content: flex-end;
    align-items: center;
    gap: 14px;
    font-size: 17px;
    line-height: 29px;
    white-space: nowrap;
  }
  .contact__icon { width: 18px; height: 18px; flex: none; }

  .back-mark {
    position: absolute;
    left: 0; right: 0;
    top: 60px;
    text-align: center;
    font-weight: 700;
    font-size: 92px;
    line-height: 1;
    letter-spacing: 12px;
    color: var(--blue);
  }
  .services {
    position: absolute;
    left: 0; right: 0;
    top: 240px;
    list-style: none;
    text-align: center;
    color: var(--ink);
    font-size: 19px;
    line-height: 27.5px;
  }
  .services .dot { color: var(--blue); margin: 0 4px; }
  .licence {
    position: absolute;
    left: 0; right: 0;
    top: 366px;
    text-align: center;
    color: var(--ink);
    font-size: 16px;
  }
</style>
</head>
<body>

<section class="card card--front" aria-label="Business card front">
  <svg class="wave" viewBox="0 0 540 308" preserveAspectRatio="none" aria-hidden="true">
    <path fill="var(--purple)" d="M0,204 C80,240 150,258 216,232 C318,192 408,78 540,60 L540,66 C410,86 322,198 220,238 C150,264 80,250 0,220 Z"/>
    <path fill="var(--blue)" d="M0,226 C80,256 150,272 222,246 C322,208 412,90 540,72 L540,308 L0,308 Z"/>
  </svg>

  <div class="brand">
    <div class="brand__mark">KTW</div>
    <div class="brand__name">COPPER LINTON PLUMBING</div>
  </div>

  <div class="contact">
    <div class="contact__name">Reid Linton</div>
    <div class="contact__line">
      <span>0427 316 902</span>
      <svg class="contact__icon" viewBox="0 0 18 18" aria-hidden="true">
        <rect x="5" y="1" width="9" height="16" rx="1.5" fill="none" stroke="var(--white)" stroke-width="1.6"/>
        <rect x="8" y="14" width="3" height="1.4" fill="var(--white)"/>
      </svg>
    </div>
    <div class="contact__line">
      <span>copperlintonplumbing@mailvane.example</span>
      <svg class="contact__icon" viewBox="0 0 18 18" aria-hidden="true">
        <rect x="2" y="5" width="14" height="9" fill="none" stroke="var(--white)" stroke-width="1.4"/>
        <path d="M2,5 L9,10 L16,5" fill="none" stroke="var(--white)" stroke-width="1.4"/>
      </svg>
    </div>
    <div class="contact__line">
      <span>Copper Linton Plumbing</span>
      <svg class="contact__icon" viewBox="0 0 18 18" aria-hidden="true">
        <rect x="2" y="2" width="14" height="14" fill="var(--white)"/>
      </svg>
    </div>
  </div>
</section>

<section class="card card--back" aria-label="Business card back">
  <div class="back-mark">KTW</div>
  <ul class="services">
    <li>Hot &amp; Cold Water Services <span class="dot">•</span> Gas Fitting</li>
    <li>Bathroom &amp; Kitchen Renovations <span class="dot">•</span> Metal Roofing &amp; Guttering</li>
    <li>New Homes &amp; Extensions <span class="dot">•</span> Hot Water Service Changeovers</li>
    <li>Drainage &amp; Stormwater Works <span class="dot">•</span> All General Plumbing &amp; Maitenance</li>
  </ul>
  <p class="licence">Lic. No 492318</p>
</section>

</body>
</html>
```